Wes Hadley Golf Teaching Rack Card

The flyer will be a rack card. Front side only. Nothing on back. 3.75 inches by 8.5 inches. Or close to that. I’d like it to be as colorful as possible and to include several logos in different places.
The brochure is to attract golfers attention and still look traditional and classy not crazy or to artsy. Golf is a very traditional sport and would just like it to look professional and welcoming so golfers no I’m credible in my teaching and they will learn something. I will send a rough idea and a sample of one I had before but use your creative skills and ingenuity to design it. You will have to put my name: Wes Hadley under the NLT logo. It is a requirement by the NLT. Also the logo size must me .0875 inches high. If possible use a gotham or Hoefler text type or something businesslike or similar for my name. Also I am sorry for the different logos available on this file because I am not tech savvy so you will have to choose the best logo and cut it out of the grouping to match what you want to do. I am sorry for all the details. I will be available all weekend if you need more info. or help. I am sure you are very skilled and can tell I am not. Sorry. I laid out a sketch for you so you know what info. verbiage is important. and where to somewhat place the logos. Up to your skill for most of it. Your design! Go for it.!

Target Market(s)

Golfers of all ages from 18-70. Men and Women.

Industry/Entity Type

Golf Industry. Teaching and learning game if golf

Font styles to use
Sans Serif
Other font styles liked:
• Mixture maybe traditional type. Easy to read.

Colors

Designer to choose only greyscale colors for use in the design.

Requirements
Must have
• My JPG golf logo and the NLT official logo. Also will send several other logos to put in. I will tell you where they should go on the rack card.
Nice to have
• Maybe a golf picture from a course with a green and flag as the one on my old brochure I’m sending or similar. It just adds color and eye catching
Should not have
• Nothing hard to read or difficult to comprehend. Pretty straight forward and quality and style in a traditional sense,

```html
<!DOCTYPE html>
<html lang="en">
<head>
<meta charset="utf-8">
<title>Wes Hadley Golf Teaching Rack Card</title>
<link rel="stylesheet" href="https://fonts.googleapis.com/css2?family=Lato:ital,wght@0,400;0,700;0,900;1,700&family=Lobster&display=swap">
<style>
  :root {
    --backdrop: #e9e9e9;
    --card: #ffffff;
    --ink: #1a1a1a;
    --mark: #333333;
    --silver-dark: #8c8c8c;
    --silver-mid: #c4c4c4;
    --silver-light: #ececec;
    --panel: #000000;
    --panel-title: #d9d9d9;
    --panel-text: #c8c8c8;
    --panel-bright: #ffffff;
    --partner-a: #6b6b6b;
  }
  * { margin: 0; padding: 0; box-sizing: border-box; }
  html, body { width: 1200px; height: 1200px; overflow: hidden; }
  body { background: var(--backdrop); font-family: "Lato", Arial, sans-serif; color: var(--ink); position: relative; }

  .rack-card {
    position: absolute; left: 362px; top: 62px; width: 476px; height: 1076px;
    background: var(--card); box-shadow: 0 2px 6px rgba(0,0,0,.15);
  }
  .rack-card > * { position: absolute; }

  .brand-mark { top: 52px; left: 0; width: 100%; display: flex; justify-content: center; align-items: center; gap: 10px; }
  .brand-mark .dot { width: 44px; height: 44px; border-radius: 50%; background: var(--mark); }
  .brand-mark .name { font-weight: 900; font-size: 40px; color: var(--mark); letter-spacing: 2px; }
  .pro-name { top: 112px; width: 100%; text-align: center; font-weight: 700; font-size: 17px; letter-spacing: 1px; color: var(--ink); }

  .website { top: 180px; width: 100%; text-align: center; font-weight: 700; font-size: 25px; }
  .contact-line { top: 220px; width: 100%; text-align: center; font-size: 14px; }
  .contact-line b { font-weight: 700; }

  .offer { top: 255px; left: 27px; width: 419px; height: 249px; display: flex; border: 2px solid var(--silver-dark); }
  .offer-title {
    width: 250px; height: 100%;
    background: linear-gradient(90deg, var(--silver-dark) 0%, var(--silver-mid) 45%, var(--silver-light) 70%, var(--silver-mid) 100%);
    display: flex; flex-direction: column; align-items: center; justify-content: center;
    font-family: "Lobster", cursive; color: #111;
  }
  .offer-title .big { font-size: 92px; line-height: .95; }
  .offer-title .small { font-size: 28px; margin-top: 4px; }
  .offer-price { flex: 1; text-align: center; padding-top: 22px; font-size: 20px; line-height: 1.25; }
  .offer-price .amount { display: block; font-weight: 900; font-size: 30px; margin-top: 22px; }
  .offer-price .reg { display: block; margin-top: 8px; }

  .includes { top: 518px; width: 100%; text-align: center; }
  .includes h2 { font-style: italic; font-weight: 700; font-size: 25px; margin-bottom: 2px; }
  .includes li { list-style: none; font-size: 19px; line-height: 25px; }

  .partners { top: 676px; left: 0; width: 100%; }
  .partner { position: absolute; font-weight: 900; font-size: 27px; }
  .partner-a { left: 34px; color: var(--partner-a); }
  .partner-b { left: 297px; color: var(--ink); }

  .silver-rule { top: 729px; left: 54px; width: 367px; height: 3px;
    background: linear-gradient(90deg, transparent, var(--silver-mid) 20%, var(--silver-mid) 80%, transparent); }

  .package { top: 749px; left: 19px; width: 437px; height: 185px; background: var(--panel); border-radius: 13px; color: var(--panel-text); }
  .package > * { position: absolute; }
  .package h3 { top: 10px; width: 100%; text-align: center; font-family: "Lobster", cursive; font-weight: 400; font-size: 32px; color: var(--panel-title); }
  .package .divider { top: 59px; left: 130px; width: 177px; height: 1px; background: linear-gradient(90deg, transparent, var(--silver-mid), transparent); }
  .package .lessons { top: 72px; left: 18px; font-size: 19px; line-height: 26px; }
  .package .deal { top: 72px; right: 18px; text-align: center; font-size: 19px; line-height: 26px; }
  .package .deal b { color: var(--panel-bright); font-weight: 900; }
  .package .note { top: 130px; width: 100%; text-align: center; font-size: 16px; line-height: 21px; color: var(--panel-text); }

  .seal { top: 962px; border-radius: 50%; }
  .seal-guarantee { left: 35px; width: 81px; height: 81px; background: radial-gradient(circle, var(--silver-mid) 0 40%, #111 42% 100%); border: 3px solid var(--silver-dark); }
  .seal-member { left: 197px; width: 85px; height: 85px; background: var(--mark); border: 4px solid var(--silver-dark); }
</style>
</head>
<body>
  <main class="rack-card">
    <div class="brand-mark"><span class="dot"></span><span class="name">NLT</span></div>
    <p class="pro-name">Wes Hadley</p>

    <p class="website">www.whadleygolf.com</p>
    <p class="contact-line">www.whadleycoach.com • <b>555-318-0427</b> • www.whadley.com</p>

    <section class="offer">
      <div class="offer-title"><span class="big">Golf</span><span class="small">Swing Analysis</span></div>
      <div class="offer-price">
        1 Hour<br>Analysis
        <span class="amount">$59.99</span>
        *One Time<br>Limited Offer
        <span class="reg">Reg 7900</span>
      </div>
    </section>

    <section class="includes">
      <h2>Includes:</h2>
      <ul>
        <li>Lorem ipsum dolor sit amet, consectetuer</li>
        <li>Lorem ipsum dolor sit amet, consectetuer</li>
        <li>Lorem ipsum dolor sit amet, consectetuer</li>
        <li>Lorem ipsum dolor sit amet, consectetuer</li>
      </ul>
    </section>

    <div class="partners">
      <span class="partner partner-a">swingframe</span>
      <span class="partner partner-b">Trackline</span>
    </div>

    <div class="silver-rule"></div>

    <section class="package">
      <h3>Special Lesson Package</h3>
      <div class="divider"></div>
      <p class="lessons">3-One Hour Lessons<br>&nbsp;&nbsp;Reg *23700</p>
      <p class="deal"><b>$225.00</b><br>(Limited Deal)</p>
      <p class="note">Lorem ipsum dolor sit amet, consectetuer<br>adipiscing elit, sed diam nonummy nibh</p>
    </section>

    <div class="seal seal-guarantee" role="img" aria-label="Satisfaction guarantee seal"></div>
    <div class="seal seal-member" role="img" aria-label="Member professional seal"></div>
  </main>
</body>
</html>
```